Business Card Design

Need a hot business card in wine colors something cool and mod please feel free to be , FUNKY and free with this .
Updates

Industry/Entity Type

Business

Contact Information for Business Card

KALIMERO HAIR DESIGN 2918 w 3rd st scottsdale az 85019 Custom modern hair design and custom color by MARCUS DOVELING 602-4813926 cell salon 480 -317-2064 email marcusdoveling@plumbox.net hours wed thru sat 7am to 6pm.

Font styles to use
Other font styles liked:
• something fun and mod.

Colors
a54599
6b449b
1b1b1b
606060

Requirements
Must have
• Apointment reminder on flip side of card.
Should not have
• Nothing boring.

```html
<!DOCTYPE html>
<html lang="en">
<head>
<meta charset="utf-8">
<title>Kalimero Hair Design – Business Card</title>
<link rel="stylesheet" href="https://fonts.googleapis.com/css2?family=Open+Sans:wght@400;600&family=Great+Vibes&display=swap">
<style>
  :root {
    --wine: #a54599;
    --violet: #6b449b;
    --violet-deep: #55338a;
    --ink: #1b1b1b;
    --grey: #606060;
    --paper: #ffffff;
    --stage: #e9e6ec;
  }
  * { box-sizing: border-box; margin: 0; padding: 0; }
  html, body { width: 1200px; height: 1023px; overflow: hidden; }
  body {
    background: var(--stage);
    font-family: "Open Sans", Arial, sans-serif;
    position: relative;
  }
  .card {
    position: absolute;
    left: 215px;
    width: 770px;
    height: 440px;
    border-radius: 26px;
    overflow: hidden;
    box-shadow: 0 6px 18px rgba(0,0,0,.18);
  }

  /* Appointment side */
  .card--back {
    top: 45px;
    background: linear-gradient(160deg, #7a52ad 0%, var(--violet) 45%, var(--violet-deep) 100%);
    color: var(--paper);
  }
  .portrait-area {
    position: absolute;
    right: 0; top: 0;
    width: 380px; height: 440px;
    background: radial-gradient(ellipse at 55% 45%, rgba(255,255,255,.16), rgba(255,255,255,0) 65%);
  }
  .back-header {
    position: absolute;
    left: 36px; top: 40px; right: 36px;
    display: flex; align-items: center;
  }
  .brand {
    display: flex; align-items: center; gap: 14px;
  }
  .brand__mark {
    width: 74px; height: 74px; border-radius: 8px;
    background: var(--wine);
  }
  .brand__name {
    font-weight: 600;
    font-size: 38px;
    line-height: 1;
    letter-spacing: 1px;
  }
  .brand__name span { display: block; font-size: 30px; letter-spacing: 1.5px; margin-top: 4px; }
  .card--back .brand__name { color: var(--paper); }
  .divider {
    width: 2px; height: 80px; margin: 0 30px;
    background: rgba(255,255,255,.6);
  }
  .appointment-title {
    font-family: "Great Vibes", cursive;
    font-size: 40px;
    color: var(--paper);
  }
  .tagline-band {
    position: absolute;
    left: 0; right: 0; top: 140px; height: 50px;
    background: var(--wine);
    display: flex; align-items: center; justify-content: center;
    font-size: 22px; letter-spacing: .5px;
  }
  .appointment-rows {
    position: absolute;
    left: 44px; right: 44px; top: 215px;
    display: grid; gap: 18px;
  }
  .appointment-row {
    display: grid;
    grid-template-columns: 1fr 220px;
    gap: 30px;
    font-size: 20px;
  }
  .field { display: flex; align-items: baseline; gap: 8px; }
  .field__line {
    flex: 1; border-bottom: 2px dotted rgba(255,255,255,.55);
  }

  /* Contact side */
  .card--front {
    top: 540px;
    background: var(--paper);
    color: var(--ink);
  }
  .card--front .brand { position: absolute; left: 50px; top: 50px; }
  .card--front .brand__mark { width: 96px; height: 96px; }
  .card--front .brand__name { color: var(--ink); font-size: 44px; }
  .card--front .brand__name span { font-size: 34px; }
  .person {
    position: absolute; left: 110px; top: 188px;
  }
  .person__name { color: var(--wine); font-size: 32px; font-weight: 400; }
  .person__title { color: var(--ink); font-size: 18px; margin-left: 70px; }
  .contacts {
    position: absolute; right: 40px; top: 280px;
    list-style: none; text-align: right;
    font-size: 18px; color: var(--ink);
    display: grid; gap: 4px;
  }
  .contacts li { display: flex; justify-content: flex-end; align-items: center; gap: 10px; }
  .icon { width: 22px; height: 22px; }
  .front-band {
    position: absolute; left: 0; right: 0; bottom: 0; height: 56px;
    background: var(--wine); color: var(--paper);
    display: flex; align-items: center; justify-content: center;
    font-size: 22px; letter-spacing: .5px;
  }
</style>
</head>
<body>

<section class="card card--back">
  <div class="portrait-area" role="img" aria-label="Faint portrait of a woman with styled hair"></div>
  <header class="back-header">
    <div class="brand">
      <div class="brand__mark"></div>
      <div class="brand__name">KALIMERO<span>Hair Design</span></div>
    </div>
    <div class="divider"></div>
    <div class="appointment-title">Your Next Appointment</div>
  </header>
  <div class="tagline-band">Custom Modern Hair Design and Custom Color</div>
  <div class="appointment-rows">
    <div class="appointment-row">
      <div class="field">Date:<span class="field__line"></span></div>
      <div class="field">Time:<span class="field__line"></span></div>
    </div>
    <div class="appointment-row">
      <div class="field">Date:<span class="field__line"></span></div>
      <div class="field">Time:<span class="field__line"></span></div>
    </div>
    <div class="appointment-row">
      <div class="field">Date:<span class="field__line"></span></div>
      <div class="field">Time:<span class="field__line"></span></div>
    </div>
    <div class="appointment-row">
      <div class="field">Date:<span class="field__line"></span></div>
      <div class="field">Time:<span class="field__line"></span></div>
    </div>
  </div>
</section>

<section class="card card--front">
  <div class="brand">
    <div class="brand__mark"></div>
    <div class="brand__name">KALIMERO<span>Hair Design</span></div>
  </div>
  <div class="person">
    <h1 class="person__name">Marcus Doveling</h1>
    <p class="person__title">Your Title</p>
  </div>
  <ul class="contacts">
    <li>602-4813926
      <svg class="icon" viewBox="0 0 22 22"><rect width="22" height="22" rx="3" fill="#6b449b"/><rect x="7" y="3" width="8" height="16" rx="1.5" fill="none" stroke="#fff" stroke-width="1.6"/><circle cx="11" cy="16" r="1" fill="#fff"/></svg>
    </li>
    <li>480 -317-2064
      <svg class="icon" viewBox="0 0 22 22"><rect width="22" height="22" rx="3" fill="#6b449b"/><path d="M4 9c0-3 14-3 14 0v1h-4V8.5H8V10H4z" fill="#fff"/><rect x="6" y="11" width="10" height="7" rx="1" fill="#fff"/><circle cx="11" cy="14.5" r="1.6" fill="#6b449b"/></svg>
    </li>
    <li>marcusdoveling@plumbox.net
      <svg class="icon" viewBox="0 0 22 22"><rect width="22" height="22" rx="3" fill="#6b449b"/><rect x="4" y="6" width="14" height="10" fill="none" stroke="#fff" stroke-width="1.6"/><path d="M4 6l7 6 7-6" fill="none" stroke="#fff" stroke-width="1.6"/></svg>
    </li>
  </ul>
  <div class="front-band">Custom Modern Hair Design and Custom Color</div>
</section>

</body>
</html>
```